Volren Goods Ltd Stationery Design Project

hi we need to design business cards, letter head, complimentary slips, scribble pads, note pads, envelopes for volren goods ltd.

please see business cards details

Kelvin Obutu

P.O Box 41873 -00312 Nairobi - Kenya
Tel: +254-733-218-904
Email: volrengoods@mailvexo.com

company name should appear on all stationery : Volren Goods Ltd

Industry/Entity Type

Business

Requirements
Must have
• kindly stick to colours in the logo

```html
<!DOCTYPE html>
<html lang="en">
<head>
<meta charset="utf-8">
<title>Volren Goods Ltd — Stationery Set</title>
<link rel="stylesheet" href="https://fonts.googleapis.com/css2?family=Questrial&family=Great+Vibes&display=swap">
<style>
  :root{
    --paper:#ffffff;
    --backdrop:#f1f1f1;
    --orange:#e5842a;
    --orange-deep:#df7a22;
    --yellow:#f0cc45;
    --blue:#34409a;
    --blue-dark:#2d3589;
    --ink:#444444;
    --muted:#8a8a8a;
  }
  *{box-sizing:border-box;margin:0;padding:0}
  html,body{width:1200px;height:1000px;overflow:hidden}
  body{position:relative;background:var(--backdrop);font-family:"Questrial",sans-serif;color:var(--ink)}
  .item{position:absolute;background:var(--paper);overflow:hidden}
  .item svg.swoosh{position:absolute;left:0;display:block}

  /* brand name block */
  .brand{position:absolute;text-align:center;color:var(--blue);font-family:"Questrial",sans-serif;line-height:.95;letter-spacing:.04em;transform:translateX(-50%)}
  .brand-dot{display:block;margin:0 auto .25em;border-radius:50%;background:var(--orange)}
  .brand-name{display:block;white-space:nowrap}

  /* letterhead */
  .letterhead{left:292px;top:98px;width:292px;height:415px}
  .letter-greeting{position:absolute;left:26px;top:118px;font-size:6.5px;font-weight:bold;color:#222}
  .letter-body{position:absolute;left:26px;top:132px;width:242px;font-size:4.9px;line-height:7.6px;color:#555;text-align:justify}
  .letter-body p{margin-bottom:7.6px}
  .letter-closing{position:absolute;right:26px;top:321px;text-align:right;font-size:5px;color:#555;line-height:9px}
  .letter-closing strong{font-size:6px;color:#222}
  .letter-footer{position:absolute;left:0;right:0;bottom:7px;text-align:center;font-size:4px;color:#fff;letter-spacing:.02em}

  /* folder */
  .folder{left:636px;top:80px;width:346px;height:436px}
  .folder-ornament{position:absolute;left:40px;top:300px;width:290px;height:136px;background:radial-gradient(ellipse at 60% 80%,rgba(255,236,170,.35),rgba(255,236,170,0) 65%)}

  /* business cards */
  .card-front{left:186px;top:550px;width:132px;height:77px}
  .card-name{position:absolute;left:8px;top:54px;font-size:4.4px;color:#fff;letter-spacing:.05em;line-height:6px}
  .card-name span{display:block;font-size:3.4px;letter-spacing:0;opacity:.9}
  .card-contact{position:absolute;right:6px;top:56px;text-align:right;font-size:3px;color:#fff;line-height:4.6px}
  .card-back{left:186px;top:646px;width:132px;height:75px;background:var(--blue)}
  .card-pattern{position:absolute;inset:0;background:radial-gradient(circle at 50% 70%,#4a55ad,var(--blue-dark) 75%)}

  /* envelopes */
  .envelope-front{left:353px;top:562px;width:328px;height:156px}
  .envelope-address{position:absolute;left:22px;top:71px;font-size:4.2px;color:var(--blue)}
  .envelope-back{left:713px;top:562px;width:328px;height:156px}
  .envelope-flap{position:absolute;left:0;top:0;width:328px;height:54px;background:var(--orange);border-bottom:1px solid #c96c1c}
  .flap-mark{position:absolute;left:156px;top:21px;width:16px;height:16px;border-radius:50%;border:1.5px solid rgba(255,255,255,.6)}

  /* notepad */
  .notepad{left:244px;top:772px;width:194px;height:176px}

  /* disc */
  .disc{position:absolute;left:470px;top:767px;width:170px;height:170px;border-radius:50%;background:var(--paper);border:1px solid #dcdcdc}
  .disc-hub{position:absolute;left:50%;top:50%;width:46px;height:46px;margin:-23px 0 0 -23px;border-radius:50%;background:radial-gradient(circle,#f1f1f1 0 9px,#c9c9c9 9px 10px,#e4e4e4 10px 16px,#d2d2d2 16px 23px)}

  /* compliment slip */
  .slip{left:742px;top:772px;width:299px;height:140px}
  .slip-title{position:absolute;left:22px;top:106px;font-family:"Great Vibes",cursive;font-size:21px;color:#fff}
  .slip-contact{position:absolute;right:12px;top:114px;text-align:left;font-size:3.6px;color:#fff;line-height:5px}
</style>
</head>
<body>

<svg width="0" height="0" style="position:absolute" aria-hidden="true">
  <defs>
    <linearGradient id="warm" x1="0" x2="1" y1="0" y2="0">
      <stop offset="0" stop-color="#efc744"/>
      <stop offset="0.55" stop-color="#eba036"/>
      <stop offset="1" stop-color="#e27d25"/>
    </linearGradient>
  </defs>
</svg>

<!-- Letterhead -->
<section class="item letterhead">
  <div class="brand" style="left:146px;top:24px;font-size:13px">
    <span class="brand-dot" style="width:14px;height:14px"></span>
    <span class="brand-name">VOLREN</span><span class="brand-name">GOODS</span>
  </div>
  <p class="letter-greeting">Dear sir / madame,</p>
  <div class="letter-body">
    <p>Thank you for choosing Volren Goods Ltd as your trusted supplier. We are pleased to confirm that your order has been received and is now being prepared for delivery. Our team will contact you shortly with shipping details, invoices and any further information you may need. We value your business and look forward to serving you again.</p>
    <p>Thank you for choosing Volren Goods Ltd as your trusted supplier. We are pleased to confirm that your order has been received and is now being prepared for delivery. Our team will contact you shortly with shipping details, invoices and any further information you may need. We value your business and look forward to serving you again.</p>
    <p>Thank you for choosing Volren Goods Ltd as your trusted supplier. We are pleased to confirm that your order has been received and is now being prepared for delivery. Our team will contact you shortly with shipping details, invoices and any further information you may need. We value your business and look forward to serving you again.</p>
    <p>Thank you for choosing Volren Goods Ltd as your trusted supplier. We are pleased to confirm that your order has been received and is now being prepared for delivery. Our team will contact you shortly with shipping details, invoices and any further information you may need. We value your business and look forward to serving you again.</p>
  </div>
  <div class="letter-closing">Yours Sincerely,<br><strong>Lena Ortis</strong></div>
  <svg class="swoosh" style="top:368px" width="292" height="47" viewBox="0 0 292 47" preserveAspectRatio="none" aria-hidden="true">
    <path d="M0,10 Q146,-2 292,14 L292,17 Q146,3 0,13Z" fill="var(--orange)"/>
    <path d="M0,16 Q146,6 292,20 V47 H0Z" fill="url(#warm)"/>
  </svg>
  <p class="letter-footer">P.O Box 41873 -00312 Nairobi - Kenya &nbsp;&nbsp; Tel: +254-733-218-904 &nbsp;&nbsp; Email: volrengoods@mailvexo.com</p>
</section>

<!-- Presentation folder -->
<section class="item folder">
  <div class="brand" style="left:173px;top:88px;font-size:22px">
    <span class="brand-dot" style="width:22px;height:22px"></span>
    <span class="brand-name">VOLREN</span><span class="brand-name">GOODS</span>
  </div>
  <svg class="swoosh" style="top:210px" width="346" height="226" viewBox="0 0 346 226" preserveAspectRatio="none" aria-hidden="true">
    <path d="M0,5 Q173,-3 346,14 L346,18 Q173,3 0,9Z" fill="var(--orange)"/>
    <path d="M0,13 Q173,7 346,22 V226 H0Z" fill="url(#warm)"/>
  </svg>
  <div class="folder-ornament" role="img" aria-label="Faint sun ornament decoration"></div>
</section>

<!-- Business card front -->
<section class="item card-front">
  <div class="brand" style="left:66px;top:9px;font-size:8px">
    <span class="brand-dot" style="width:8px;height:8px"></span>
    <span class="brand-name">VOLREN</span><span class="brand-name">GOODS</span>
  </div>
  <svg class="swoosh" style="top:42px" width="132" height="35" viewBox="0 0 132 35" preserveAspectRatio="none" aria-hidden="true">
    <path d="M0,6 Q66,-1 132,8 L132,10 Q66,2 0,8Z" fill="var(--orange)"/>
    <path d="M0,10 Q66,5 132,12 V35 H0Z" fill="url(#warm)"/>
  </svg>
  <p class="card-name">JONAH KELLER<span>Director</span></p>
  <p class="card-contact">P.O Box 41873 -00312 Nairobi - Kenya<br>Tel: +254-733-218-904<br>Email: volrengoods@mailvexo.com</p>
</section>

<!-- Business card back -->
<section class="item card-back">
  <div class="card-pattern" role="img" aria-label="Swirling sun-ray pattern in blue tones"></div>
  <div class="brand" style="left:66px;top:22px;font-size:9px;color:var(--orange)">
    <span class="brand-dot" style="width:9px;height:9px"></span>
    <span class="brand-name">VOLREN</span><span class="brand-name">GOODS</span>
  </div>
</section>

<!-- DL envelope front -->
<section class="item envelope-front">
  <div class="brand" style="left:56px;top:20px;font-size:13px">
    <span class="brand-dot" style="width:13px;height:13px"></span>
    <span class="brand-name">VOLREN</span><span class="brand-name">GOODS</span>
  </div>
  <p class="envelope-address">P.O Box 41873 -00312 Nairobi - Kenya</p>
  <svg class="swoosh" style="top:110px" width="328" height="46" viewBox="0 0 328 46" preserveAspectRatio="none" aria-hidden="true">
    <path d="M0,4 Q164,-2 328,12 L328,15 Q164,2 0,7Z" fill="var(--orange)"/>
    <path d="M0,12 Q164,6 328,19 V46 H0Z" fill="url(#warm)"/>
  </svg>
</section>

<!-- DL envelope back -->
<section class="item envelope-back">
  <div class="envelope-flap"><span class="flap-mark"></span></div>
</section>

<!-- Notepad -->
<section class="item notepad">
  <div class="brand" style="left:97px;top:22px;font-size:13px">
    <span class="brand-dot" style="width:13px;height:13px"></span>
    <span class="brand-name">VOLREN</span><span class="brand-name">GOODS</span>
  </div>
  <svg class="swoosh" style="top:80px" width="194" height="96" viewBox="0 0 194 96" preserveAspectRatio="none" aria-hidden="true">
    <path d="M0,4 Q97,-2 194,10 L194,13 Q97,2 0,7Z" fill="var(--orange)"/>
    <path d="M0,11 Q97,6 194,16 V96 H0Z" fill="url(#warm)"/>
  </svg>
</section>

<!-- CD label -->
<div class="disc">
  <div class="brand" style="left:85px;top:22px;font-size:10px">
    <span class="brand-dot" style="width:10px;height:10px"></span>
    <span class="brand-name">VOLREN</span><span class="brand-name">GOODS</span>
  </div>
  <div class="disc-hub"></div>
</div>

<!-- Compliment slip -->
<section class="item slip">
  <div class="brand" style="left:56px;top:18px;font-size:13px">
    <span class="brand-dot" style="width:13px;height:13px"></span>
    <span class="brand-name">VOLREN</span><span class="brand-name">GOODS</span>
  </div>
  <svg class="swoosh" style="top:82px" width="299" height="58" viewBox="0 0 299 58" preserveAspectRatio="none" aria-hidden="true">
    <path d="M0,4 Q150,-2 299,11 L299,14 Q150,2 0,7Z" fill="var(--orange)"/>
    <path d="M0,12 Q150,6 299,18 V58 H0Z" fill="url(#warm)"/>
  </svg>
  <p class="slip-title">With Compliments</p>
  <p class="slip-contact">P.O Box 41873 -00312 Nairobi - Kenya<br>Tel: +254-733-218-904 &nbsp; Email: volrengoods@mailvexo.com</p>
</section>

</body>
</html>
```